Professional and Modern Company Letterhead for Fintech Startup

Brisk lending is a fintech startup that provides home financing.

Our company requires letterhead in Microsoft word format. Colors must come from our ADA compliant doc.

Company logo, equal housing opportunity logo, and legal language must be included somewhere on the document.

We'd love an option that maximizes space on the page for text vs have design take up the entire thing.

Target Market(s)

Partners, clients, and employees

Industry/Entity Type

Finance

Font styles to use
Sans Serif

Requirements
Must have
• Must use company colors that are ADA compliant (see attachment). Must include logo in a prominent position. Must include equal housing opportunity logo and legal info at the bottom:

©Brisk Lending LLC. NMLS #5093374 | 4716 Harlow Avenue #204, Larkfield, NE 68912 | Not available in all states | 800.437.5068 | help@brisklending-example.com
Nice to have
• Something modern and clean.

```html
<!DOCTYPE html>
<html lang="en">
<head>
<meta charset="utf-8">
<title>Brisk lending — Letterhead</title>
<link rel="stylesheet" href="https://fonts.googleapis.com/css2?family=Open+Sans:wght@400;600;700&display=swap">
<style>
  :root {
    --backdrop: #d9dcdd;
    --paper: #ffffff;
    --navy: #1f2a44;
    --slate: #6b6f78;
    --teal: #45b8d0;
    --text-grey: #6a6d73;
    --ink: #1b1b1b;
  }
  * { margin: 0; padding: 0; box-sizing: border-box; }
  html, body {
    width: 1200px; height: 784px; overflow: hidden;
    background: var(--backdrop);
    font-family: "Open Sans", Arial, sans-serif;
  }
  .letterhead {
    position: absolute; left: 314px; top: 22px;
    width: 572px; height: 740px;
    background: var(--paper);
    box-shadow: 0 2px 10px rgba(0,0,0,.12);
  }
  .brand {
    position: absolute; left: 32px; top: 30px;
    display: flex; align-items: center; gap: 8px;
  }
  .brand-mark { width: 14px; height: 14px; background: var(--teal); }
  .brand-name {
    font-weight: 700; font-size: 26px; color: var(--teal);
    letter-spacing: -0.5px; line-height: 1;
  }
  .contact {
    position: absolute; left: 190px; top: 62px; width: 280px;
    text-align: right; color: var(--text-grey); font-size: 7px; line-height: 1.7;
  }
  .contact-company { color: var(--navy); font-weight: 700; font-size: 8px; }
  .contact-line { display: flex; justify-content: flex-end; align-items: center; gap: 4px; }
  .icon { width: 7px; height: 7px; flex: none; }
  .contact-rule { position: absolute; left: 186px; top: 104px; width: 292px; height: 6px; }
  .housing-badge {
    position: absolute; left: 498px; top: 86px; width: 40px; height: 40px;
    border: 3px solid var(--ink);
  }
  .legal {
    position: absolute; left: 40px; right: 40px; top: 672px;
    text-align: center; color: var(--navy); font-size: 7.4px; line-height: 1.55;
  }
  .footer-bands { position: absolute; left: 0; bottom: 0; width: 572px; height: 34px; }
</style>
</head>
<body>
  <main class="letterhead">
    <header>
      <div class="brand">
        <span class="brand-mark"></span>
        <span class="brand-name">Brisk lending</span>
      </div>

      <div class="contact">
        <div class="contact-company">Brisk Lending Inc.</div>
        <div class="contact-line">
          <svg class="icon" viewBox="0 0 10 10"><circle cx="5" cy="5" r="4.3" fill="none" stroke="#6a6d73"/><circle cx="5" cy="4.3" r="1.4" fill="#6a6d73"/></svg>
          <span>4716 Harlow Avenue #204, Larkfield, NE 68912</span>
          <svg class="icon" viewBox="0 0 10 10"><circle cx="5" cy="5" r="4.3" fill="none" stroke="#6a6d73"/><path d="M3.5 2.8v1.6c0 1.4 1 2.4 2.4 2.4h.9" fill="none" stroke="#6a6d73"/></svg>
          <span>1.888.514.7702</span>
        </div>
        <div class="contact-line">
          <svg class="icon" viewBox="0 0 10 10"><circle cx="5" cy="5" r="4.3" fill="none" stroke="#6a6d73"/><rect x="2.8" y="3.4" width="4.4" height="3.2" fill="none" stroke="#6a6d73" stroke-width=".8"/></svg>
          <span>hello@brisklending-example.com</span>
          <svg class="icon" viewBox="0 0 10 10"><circle cx="5" cy="5" r="4.3" fill="none" stroke="#6a6d73"/><path d="M1 5h8M5 1c-2 2.5-2 5.5 0 8M5 1c2 2.5 2 5.5 0 8" fill="none" stroke="#6a6d73" stroke-width=".7"/></svg>
          <span>www.brisklending-example.com</span>
        </div>
      </div>

      <svg class="contact-rule" viewBox="0 0 292 6" aria-hidden="true">
        <line x1="3" y1="3" x2="289" y2="3" stroke="#1f2a44" stroke-width="1.2"/>
        <rect x="0" y="0" width="6" height="6" fill="#6b6f78"/>
        <rect x="286" y="0" width="6" height="6" fill="#6b6f78"/>
      </svg>

      <div class="housing-badge" role="img" aria-label="Equal housing opportunity badge"></div>
    </header>

    <footer>
      <p class="legal">
        ©Brisk Lending LLC. NMLS #5093374 | 4716 Harlow Avenue #204, Larkfield, NE 68912 | Not available in all states<br>
        800.437.5068 | help@brisklending-example.com
      </p>
      <svg class="footer-bands" viewBox="0 0 572 34" aria-hidden="true">
        <polygon points="0,8 250,8 244,18 0,18" fill="#1f2a44"/>
        <polygon points="256,8 572,8 572,18 250,18" fill="#6b6f78"/>
        <rect x="0" y="26" width="572" height="5" fill="#1f2a44"/>
      </svg>
    </footer>
  </main>
</body>
</html>
```